Jewelers Website

This is for the DESIGN ONLY.
I am a software programmer and will be doing the development.
New website design for
www.lunagemcraft.com.au
Need a fresh new look for an online only jewellery business who produce their jewellery by hand. I would like it designed in a parallax style. Feel free to recommend fonts to use for the site. This is an Australian based company located in NSW so shots of sites in NSW might make nice background images.
http://plaxorin.me/demo/#theme=parallax
To contain the below sections
About Us
Contact Us
Gallery
Testimonials
Diamond Types
The colour scheme is to be Black / White and Silver.
With the Parallax style there will be moving sections and images for added impact.
Target Market(s)
Young Adults mainly engagement jewellery

```html
<!DOCTYPE html>
<html lang="en">
<head>
<meta charset="utf-8">
<title>Luna Gemcraft — Diamond Engagement Rings &amp; Jewellery</title>
<link href="https://fonts.googleapis.com/css2?family=Didact+Gothic&display=swap" rel="stylesheet">
<style>
:root{
  --ink:#ffffff;
  --muted:#c9c9c9;
  --soft:#9a9a9a;
  --bg-dark:#1c1c1c;
  --bg-section:#222222;
  --bg-footer:#1a1a1a;
  --field:#ffffff;
  --silver:#d8d8d8;
  --social-1:#3b5998;
  --social-2:#1da1f2;
  --social-3:#4d7fa5;
  --social-4:#cb2027;
  --social-5:#dd4b39;
}
*{box-sizing:border-box;margin:0;padding:0}
html,body{width:1200px;height:3232px;overflow:hidden;background:var(--bg-dark)}
body{font-family:"Didact Gothic",sans-serif;color:var(--ink);position:relative}
.section{position:absolute;left:0;width:1200px;text-align:center}
.section-title{font-size:34px;letter-spacing:1px;text-transform:uppercase;font-weight:400}
.intro{font-size:13.5px;line-height:24px;color:var(--muted);width:1054px;margin:20px auto 0}

/* header */
.site-header{position:absolute;top:0;left:0;width:1200px;height:84px;background:rgba(20,20,20,.85);z-index:2}
.brand{position:absolute;left:72px;top:20px;font-size:22px;line-height:24px;color:var(--ink);text-transform:uppercase;letter-spacing:1px;width:160px}
.main-nav{position:absolute;right:72px;top:50px;display:flex;gap:40px;font-size:14px}

/* hero */
.hero{top:0;height:592px;background:linear-gradient(110deg,#0d0d0d 0%,#1d1d1d 55%,#3a3a3a 75%,#151515 100%)}
.hero-photo{position:absolute;left:520px;top:0;width:680px;height:592px;background:radial-gradient(ellipse at 60% 35%,#8a8a8a 0%,#3c3c3c 35%,rgba(20,20,20,0) 70%)}
.hero-copy{position:absolute;left:72px;top:200px;width:460px;text-align:left}
.hero-copy h1{font-size:43px;line-height:52px;font-weight:400}
.hero-copy p{margin-top:16px;font-size:15px;line-height:22px;color:var(--muted)}
.dots{position:absolute;display:flex;gap:8px}
.dot{width:11px;height:11px;background:var(--ink);border-radius:2px}
.dot.off{background:#777}
.dots.round .dot{border-radius:50%;width:9px;height:9px}

/* about */
.about{top:592px;height:524px;background:linear-gradient(180deg,#2a2f31 0%,#1e2527 50%,#223026 100%)}
.about .section-title{margin-top:68px}
.about-text{width:1050px;margin:28px auto 0;font-size:12.5px;line-height:22px;color:var(--muted)}
.about-text strong{color:var(--ink);font-weight:400}
.signoff{margin-top:22px;font-size:12.5px;line-height:22px;color:var(--muted)}
.signoff .name{color:var(--ink)}

/* gallery */
.gallery{top:1116px;height:634px;background:var(--bg-section)}
.gallery .section-title{margin-top:52px}
.card-grid{position:absolute;left:73px;display:grid;grid-template-columns:repeat(4,243px);column-gap:27px;row-gap:26px}
.card .thumb{width:243px;height:136px;display:block}
.card .label{margin-top:16px;font-size:15px}

/* testimonials */
.testimonials{top:1750px;height:380px;background:linear-gradient(180deg,#3a4a5a 0%,#2c3947 55%,#1d252d 100%)}
.testimonials .section-title{margin-top:30px}
.quote{width:1000px;margin:22px auto 0;font-size:13.5px;line-height:24px;font-style:italic;color:var(--muted)}
.quote-mark{position:absolute;top:104px;font-size:40px;font-weight:700;line-height:40px}

/* diamond types */
.types{top:2130px;height:480px;background:var(--bg-section)}
.types .section-title{margin-top:50px}

/* contact */
.contact{top:2610px;height:510px;background:linear-gradient(180deg,#232a33 0%,#1b2027 60%,#12161b 100%)}
.contact .section-title{margin-top:48px}
.contact .tagline{font-size:13px;color:var(--muted);margin-top:6px}
.contact-form{position:absolute;left:60px;top:160px;width:490px;text-align:right}
.field{display:flex;align-items:flex-start;justify-content:flex-end;gap:14px;margin-bottom:14px;font-size:13px}
.field span{padding-top:8px}
.field i{display:block;width:330px;height:38px;background:var(--field)}
.field.tall i{height:114px}
.submit{display:inline-block;margin-top:4px;margin-right:0;background:var(--field);color:#222;font-size:13px;letter-spacing:1px;padding:7px 20px}
.offices{position:absolute;left:704px;top:158px;width:422px;display:flex;text-align:left}
.office{width:237px;font-size:11.5px;line-height:20px;color:var(--muted)}
.office h3{font-size:16px;font-weight:400;color:var(--ink);margin-bottom:4px}
.map{position:absolute;left:704px;top:248px;width:422px;height:228px;background:linear-gradient(135deg,#e4e4e4,#cfcfcf)}

/* footer */
.site-footer{position:absolute;top:3120px;left:0;width:1200px;height:112px;background:var(--bg-footer)}
.copyright{position:absolute;left:72px;top:14px;font-size:10px;color:var(--soft)}
.social{position:absolute;right:72px;top:9px;display:flex;gap:6px}
.social i{display:block;width:26px;height:26px}
</style>
</head>
<body>

<header class="site-header">
  <div class="brand">Luna Gemcraft</div>
  <nav class="main-nav">
    <span>Home</span><span>About Us</span><span>Gallery</span><span>Testimonials</span><span>Diamond Types</span><span>Contact Us</span>
  </nav>
</header>

<section class="section hero">
  <div class="hero-photo" role="img" aria-label="Close-up of a diamond solitaire engagement ring on a dark reflective surface"></div>
  <div class="hero-copy">
    <h1>Diamond Engagement Rings &amp; Jewellery</h1>
    <p>At Luna Gemcraft we specialise in creating beautiful jewellery and diamond engagement rings using the very best diamonds, gemstones and precious metals from Australia and around the world.</p>
  </div>
  <div class="dots" style="left:73px;top:541px"><i class="dot off"></i><i class="dot"></i><i class="dot"></i><i class="dot"></i></div>
</section>

<section class="section about" role="img" aria-label="Background view over a Sydney harbourside city with bridge and buildings">
  <h2 class="section-title">About Us</h2>
  <div class="about-text">
    At Luna Gemcraft we are passionate about fine jewellery and gems. We feature one of a kind, original and elegant, handmade pieces. Luna Gemcraft handmade jewellery is crafted using exceptional quality metals, integrating designs that are innovative, creative, and unique.<br>
    After you have consulted with our experienced staff – our highly trained and experienced jewellers hand-make every piece of finely crafted jewellery with a level of care and attention that cannot be matched by machines. Our custom jewellery is Australian-made in our Sydney workshop.<br>
    With our combination of one-to-one customer service, our deep knowledge and experience, we can help you create unique jewellery that cannot be found in any jewellery store. Better still, because we don't waste money on expensive city shopfronts, we can offer you amazing value on the most beautiful jewellery.<br><br>
    <strong>We look forward to helping you create your perfect diamond engagement and wedding rings.</strong>
  </div>
  <div class="signoff">Regards,<br><span class="name">Daniel Mercer</span><br>Diamantaire<br>Diamond Merchant</div>
</section>

<section class="section gallery">
  <h2 class="section-title">Gallery</h2>
  <p class="intro">Aliquam molestie, mi et imperdiet euismod, dui purus auctor tellus, et interdum lacus lectus et ante. Sed accumsan sollicitudin sapien, sit amet adipiscing turpis gravida ac. In congue, neque ac lobortis volutpat, libero mauris varius mi, vitae suscipit ipsum ligula vitae risus.</p>
  <div class="card-grid" style="top:200px">
    <div class="card"><i class="thumb" role="img" aria-label="Stacked diamond rings in white and rose gold" style="background:linear-gradient(135deg,#0c0c0c,#5a5a5a,#0c0c0c)"></i><div class="label">Product Name</div></div>
    <div class="card"><i class="thumb" role="img" aria-label="Diamond tennis bracelet" style="background:linear-gradient(135deg,#111,#6b6b6b,#1a1a1a)"></i><div class="label">Product Name</div></div>
    <div class="card"><i class="thumb" role="img" aria-label="Diamond hoop earrings on red" style="background:linear-gradient(135deg,#1a0a0a,#7a2020,#2a0c0c)"></i><div class="label">Product Name</div></div>
    <div class="card"><i class="thumb" role="img" aria-label="Yellow gemstone ring" style="background:linear-gradient(135deg,#f2f2f2,#d49a2a,#ececec)"></i><div class="label">Product Name</div></div>
    <div class="card"><i class="thumb" role="img" aria-label="Pink gemstone pendant on pink background" style="background:linear-gradient(135deg,#e7a5bd,#c45a84,#e9b2c6)"></i><div class="label">Product Name</div></div>
    <div class="card"><i class="thumb" role="img" aria-label="Jewellery set on grey stones" style="background:linear-gradient(135deg,#b9b9b9,#4a4a4a,#9d9d9d)"></i><div class="label">Product Name</div></div>
    <div class="card"><i class="thumb" role="img" aria-label="Pair of diamond wedding rings on white" style="background:linear-gradient(135deg,#f4f4f4,#a9a9a9,#f0f0f0)"></i><div class="label">Product Name</div></div>
    <div class="card"><i class="thumb" role="img" aria-label="Diamond necklace on red roses" style="background:linear-gradient(135deg,#5a0612,#b51a2c,#4a0610)"></i><div class="label">Product Name</div></div>
  </div>
</section>

<section class="section testimonials" role="img" aria-label="Background view of Sydney Harbour with the opera house and bridge">
  <h2 class="section-title">Testimonials</h2>
  <span class="quote-mark" style="left:74px">&ldquo;</span>
  <span class="quote-mark" style="right:74px">&rdquo;</span>
  <p class="quote">Aliquam molestie, mi et imperdiet euismod, dui purus auctor tellus, et interdum lacus lectus et ante. Sed accumsan sollicitudin sapien, sit amet adipiscing turpis gravida ac. In congue, neque ac lobortis volutpat, libero mauris varius mi, vitae suscipit ipsum ligula vitae risus. Duis aliquam nibh a dui iaculis viverra id a velit. Vivamus egestas risus in magna varius commodo. Sed semper viverra egestas.</p>
  <div class="signoff" style="margin-top:20px"><span class="name">Daniel Mercer</span><br>Diamantaire<br>Diamond Merchant</div>
  <div class="dots round" style="left:576px;top:344px"><i class="dot"></i><i class="dot off"></i><i class="dot off"></i></div>
</section>

<section class="section types">
  <h2 class="section-title">Diamond Types</h2>
  <p class="intro">Aliquam molestie, mi et imperdiet euismod, dui purus auctor tellus, et interdum lacus lectus et ante. Sed accumsan sollicitudin sapien, sit amet adipiscing turpis gravida ac. In congue, neque ac lobortis volutpat, libero mauris varius mi, vitae suscipit ipsum ligula vitae risus.</p>
  <div class="card-grid" style="top:196px">
    <div class="card"><i class="thumb" role="img" aria-label="Large clear round diamond" style="background:linear-gradient(135deg,#f0f0f0,#7a7a7a,#dcdcdc)"></i><div class="label">Product Name</div></div>
    <div class="card"><i class="thumb" role="img" aria-label="Scattered loose clear diamonds" style="background:linear-gradient(135deg,#e9eef2,#8c959c,#eef2f5)"></i><div class="label">Product Name</div></div>
    <div class="card"><i class="thumb" role="img" aria-label="Pink heart-shaped diamonds" style="background:linear-gradient(135deg,#ffffff,#e03d8f,#ffffff)"></i><div class="label">Product Name</div></div>
    <div class="card"><i class="thumb" role="img" aria-label="Green and red gemstones on white" style="background:linear-gradient(135deg,#f2f2f2,#2b7a3c 50%,#b51a2c 80%,#eaeaea)"></i><div class="label">Product Name</div></div>
  </div>
  <div class="dots round" style="left:576px;top:418px"><i class="dot"></i><i class="dot off"></i><i class="dot off"></i></div>
</section>

<section class="section contact" role="img" aria-label="Background view of Sydney city skyline across the water">
  <h2 class="section-title">Contact Us</h2>
  <p class="tagline">Wanna Talk?...Drop by and say hi...</p>
  <div class="contact-form">
    <div class="field"><span>Full Name</span><i></i></div>
    <div class="field"><span>Your Email Address</span><i></i></div>
    <div class="field"><span>Contact No.</span><i></i></div>
    <div class="field tall"><span>Contact No.</span><i></i></div>
    <span class="submit">SUBMIT</span>
  </div>
  <div class="offices">
    <div class="office"><h3>Sydney</h3>Hollowbrook NSW 2290, Australia<br>Phone +61 (0)2 9000 4812</div>
    <div class="office"><h3>Germany</h3>40210 Lindenfeld, Germany<br>Phone +49 (0)2100 5550192</div>
  </div>
  <div class="map" role="img" aria-label="Street map of the Sydney office area with a location pin">
    <svg width="422" height="228" viewBox="0 0 422 228"><path d="M211 70c-12 0-21 9-21 21 0 16 21 38 21 38s21-22 21-38c0-12-9-21-21-21z" fill="#222"/><circle cx="211" cy="91" r="7" fill="#ddd"/></svg>
  </div>
</section>

<footer class="site-footer">
  <p class="copyright">© Copyright 2002–2014 Luna Gemcraft Pty Ltd (ABN 12 345 678 901). Luna Gemcraft also trades as Daniel Mercer.</p>
  <div class="social">
    <i style="background:var(--social-1)"></i><i style="background:var(--social-2)"></i><i style="background:var(--social-3)"></i><i style="background:var(--social-4)"></i><i style="background:var(--social-5)"></i>
  </div>
</footer>

</body>
</html>
```